Glass repair Packaging Design Project

The product is a glass scratch repair kit inside a clear, plastic clamshell pack.
Two covers need to be designed: one for the front and one for the back of the clamshell pack, both 150mm(height) x 145mm(width).

The scratch repair kit comes in 2 sizes: 2" repair pads and 3" repair pads. Each size kit comes in 3 grades: light scratch removal, medium scratch removal and deep scratch removal.

The main packaging will stay the same for every kit but needs an area on the front cover to say size and grade e.g

2" repair pad, light scratch repair
or
3" repair pad, deep scratch repair

The kit is for the DIY market and so "DIY" needs to be on the front cover quite prominently.
"Drill required but not included" to be on back cover.

Repairable damage includes:
Scuffs
Scratches
Water marks
Acid marks
Wiper blade marks

(front cover)
Glass types suitable for repair include:
patio doors
window units
glass shower screens
glass tables
glass fish tanks
automotive glass
marine glass
domestic glass

The back cover of the pack needs to say the kit contents

This kit contains:
instructions
micro fibre cloth
dust mask
abrasive discs
50ml polishing compound
polishing pads
spray bottle
backing pad for drill

On the bottom of the back cover
www.panelbrightstore.co.uk

Industry/Entity Type

Automotive

Requirements
Must have
• The colour scheme must work with the logo colours. The logo is black and green.

```html
<!DOCTYPE html>
<html lang="en">
<head>
<meta charset="utf-8">
<title>Panelbright – Scratch Repair Kit Front Cover</title>
<link rel="stylesheet" href="https://fonts.googleapis.com/css2?family=Fira+Sans+Condensed:ital,wght@0,400;0,500;0,700;0,800;1,400;1,500;1,700&display=swap">
<style>
  :root {
    --backdrop: #524843;
    --card: #f2f2f2;
    --ink: #111111;
    --grey-text: #6b6b6b;
    --green: #5aaa1e;
    --green-bright: #6cc02a;
    --diy-red: #8a0000;
    --window: #524843;
    --window-text: #c9b49a;
    --white: #ffffff;
  }
  * { box-sizing: border-box; margin: 0; padding: 0; }
  html, body {
    width: 1200px; height: 900px; overflow: hidden;
    background: var(--backdrop);
    font-family: "Fira Sans Condensed", "Arial Narrow", sans-serif;
  }
  .cover {
    position: absolute; left: 238px; top: 65px;
    width: 720px; height: 743px;
    border-radius: 44px;
    background: radial-gradient(ellipse at 55% 75%, #ffffff 0%, #f4f6f7 45%, var(--card) 100%);
    overflow: hidden;
    box-shadow: 0 10px 22px rgba(0,0,0,.45);
  }
  .hang-hole {
    position: absolute; left: 326px; top: 39px;
    width: 70px; height: 22px; border-radius: 11px;
    background: #2a221f;
  }
  .hang-hole::before {
    content: ""; position: absolute; left: 27px; top: -7px;
    width: 16px; height: 16px; border-radius: 50%; background: #2a221f;
  }
  .diy-corner {
    position: absolute; right: 0; top: 0;
    width: 209px; height: 213px;
    background: var(--diy-red);
    clip-path: polygon(0 0, 100% 0, 100% 100%);
  }
  .diy-label {
    position: absolute; right: -48px; top: 36px;
    width: 220px; transform: rotate(45deg);
    text-align: center; color: var(--white);
  }
  .diy-label .diy { font-size: 74px; font-weight: 800; line-height: .9; letter-spacing: -1px; }
  .diy-label .drill { font-size: 12.5px; font-weight: 500; margin-top: 2px; white-space: nowrap; }
  .brand-mark {
    position: absolute; left: 74px; top: 78px;
    width: 90px; height: 90px; border-radius: 50%;
    background: var(--green-bright);
  }
  .brand-name {
    position: absolute; left: 202px; top: 80px;
    font-size: 82px; font-weight: 800; line-height: 1;
    letter-spacing: -2px; color: var(--ink); white-space: nowrap;
  }
  .brand-tagline {
    position: absolute; left: 252px; top: 164px;
    font-size: 16px; font-weight: 500; color: var(--grey-text); white-space: nowrap;
  }
  .damage-title {
    position: absolute; left: 0; top: 233px; width: 144px;
    font-size: 12px; font-style: italic; text-align: right; color: var(--ink);
    white-space: nowrap; letter-spacing: -.2px; padding-right: 4px;
  }
  .damage-list { position: absolute; left: 0; top: 250px; width: 144px; }
  .damage-tile {
    position: relative; height: 67px; margin-bottom: 2px;
    display: flex; align-items: flex-end; justify-content: flex-end;
    padding: 0 5px 3px 0;
  }
  .damage-tile span {
    color: var(--white); font-size: 12.5px; font-weight: 700; font-style: italic;
    text-shadow: 0 1px 2px rgba(0,0,0,.8);
  }
  .tile-scuffs { background: linear-gradient(135deg, #b8b8ae, #9c9c93); }
  .tile-scratches { background: linear-gradient(135deg, #6e6e6e, #2e2e2e); }
  .tile-watermarks { background: linear-gradient(180deg, #3e5478, #1e2a40); }
  .tile-acid { background: radial-gradient(circle at 45% 60%, #c7c7c7, #5a5a5a 70%); }
  .tile-wiper { background: linear-gradient(160deg, #8d8d8d, #2a2a2a); }
  .product-window {
    position: absolute; left: 314px; top: 199px;
    width: 202px; height: 331px; border-radius: 70px 70px 56px 56px;
    background: var(--window);
    display: flex; align-items: flex-start; justify-content: center;
    padding-top: 108px;
    color: var(--window-text); font-size: 22px; font-style: italic;
    line-height: 1.1; text-align: center;
  }
  .suitable {
    position: absolute; left: 537px; top: 258px; width: 180px;
  }
  .suitable h2 {
    color: var(--green); font-size: 21px; font-weight: 700; font-style: italic;
    line-height: 1; margin-bottom: 6px;
  }
  .suitable ul { list-style: none; }
  .suitable li {
    font-size: 18px; line-height: 24.2px; color: var(--ink);
    display: flex; align-items: center; white-space: nowrap;
  }
  .suitable li::before {
    content: ""; width: 9px; height: 9px; border-radius: 50%;
    background: var(--green); margin-right: 6px; flex: none;
  }
  .pad-badge { position: absolute; left: 95px; top: 476px; width: 530px; height: 530px; }
  .grade {
    position: absolute; left: 369px; top: 569px;
    color: var(--white);
  }
  .grade h3 { color: var(--green); font-size: 17px; font-weight: 700; margin-bottom: 7px; }
  .grade li {
    list-style: none; display: flex; align-items: center;
    font-size: 14px; font-style: italic; margin-bottom: 6px;
  }
  .grade li::before {
    content: ""; width: 17px; height: 19px; background: var(--white); margin-right: 6px;
  }
</style>
</head>
<body>
  <main class="cover">
    <div class="hang-hole"></div>

    <div class="diy-corner"></div>
    <div class="diy-label">
      <div class="diy">D.I.Y.</div>
      <div class="drill">DRILL REQUIRED BUT NOT INCLUDED</div>
    </div>

    <div class="brand-mark"></div>
    <div class="brand-name">panelbright</div>
    <div class="brand-tagline">THE ULTIMATE SCRATCH REPAIR KIT</div>

    <p class="damage-title">Repairable damage includes:</p>
    <div class="damage-list">
      <div class="damage-tile tile-scuffs" role="img" aria-label="Photo of scuffed glass"><span>SCUFFS</span></div>
      <div class="damage-tile tile-scratches" role="img" aria-label="Photo of scratched glass"><span>SCRATCHES</span></div>
      <div class="damage-tile tile-watermarks" role="img" aria-label="Photo of watermarks on glass"><span>WATERMARKS</span></div>
      <div class="damage-tile tile-acid" role="img" aria-label="Photo of acid marks on glass"><span>ACID MARKS</span></div>
      <div class="damage-tile tile-wiper" role="img" aria-label="Photo of wiper blade marks on a windscreen"><span>WIPER BLADE MARKS</span></div>
    </div>

    <div class="product-window">SEE THRU<br>WINDOW TO<br>SHOW PRODUCTS<br>IN REAR</div>

    <section class="suitable">
      <h2>Suitable glass restoration for:</h2>
      <ul>
        <li>patio doors</li>
        <li>window units</li>
        <li>glass shower screens</li>
        <li>glass tables</li>
        <li>glass fish tanks</li>
        <li>automotive glass</li>
        <li>marine glass</li>
        <li>domestic glass</li>
      </ul>
    </section>

    <svg class="pad-badge" viewBox="0 0 530 530">
      <defs>
        <radialGradient id="padTone" cx="50%" cy="55%" r="55%">
          <stop offset="0" stop-color="#9a9a9a"/>
          <stop offset=".5" stop-color="#4a4a4a"/>
          <stop offset="1" stop-color="#1e1e1e"/>
        </radialGradient>
        <clipPath id="padLeft"><rect x="0" y="0" width="265" height="530"/></clipPath>
        <clipPath id="padRight"><rect x="265" y="0" width="265" height="530"/></clipPath>
        <path id="padArc" d="M 48 265 A 217 217 0 0 1 482 265"/>
      </defs>
      <circle cx="265" cy="265" r="265" fill="#ffffff"/>
      <circle cx="265" cy="265" r="258" fill="#000000"/>
      <g role="img" aria-label="Photo of the repair pad">
        <circle cx="265" cy="290" r="215" fill="url(#padTone)" clip-path="url(#padLeft)"/>
        <circle cx="265" cy="290" r="215" fill="#151515" clip-path="url(#padRight)"/>
      </g>
      <text font-family="Fira Sans Condensed, sans-serif" font-size="35" font-weight="700" fill="#5aaa1e" letter-spacing="1">
        <textPath href="#padArc" startOffset="50%" text-anchor="middle">3" REPAIR PAD INSIDE</textPath>
      </text>
    </svg>

    <section class="grade">
      <h3>GRADE:</h3>
      <ul>
        <li>light scratch removal</li>
        <li>medium scratch removal</li>
        <li>deep scratch removal</li>
      </ul>
    </section>
  </main>
</body>
</html>
```